Business card and stationary for LOGISTICS company | ||
HAULVEX 514K | ||
Use same font as used in my logo | ||
Corporate Modern Professional Simple |
Oleksa | ||
Air and Sea freight from China to Ukraine | ||
Beijing, Lunmao Plaza C4-517K | ||
beijing@haulvex514k.com | ||
www.haulvex514k.com | ||
skype: mvoloshenko | ||
This business card would be given to the new registered client. After registration client receives his own client-number for air and for sea freight. I would need 2 lines on the back with plane and boat logo in front on it so I can write the clients number | ||

```html
<!DOCTYPE html>
<html lang="en">
<head>
<meta charset="utf-8">
<title>HAULVEX 514K – Business Card</title>
<link rel="stylesheet" href="https://fonts.googleapis.com/css2?family=Open+Sans:wght@400;600;700;800&display=swap">
<style>
  :root {
    --backdrop: #e9e7e3;
    --frame-blue: #3a63c4;
    --frame-blue-dark: #2d4fa3;
    --edge-grey: #b9bcc3;
    --card-white: #ffffff;
    --brand-red: #e0262b;
    --name-blue: #2a58b8;
    --text-dark: #3b3d42;
    --divider: #8a8d93;
    --icon-blue: #3467c6;
  }
  * { box-sizing: border-box; margin: 0; padding: 0; }
  html, body {
    width: 1200px; height: 902px; overflow: hidden;
    background: var(--backdrop);
    font-family: "Open Sans", Arial, sans-serif;
  }
  .business-card {
    position: absolute; left: 100px; top: 165px;
    width: 1000px; height: 572px;
    background: linear-gradient(160deg, var(--frame-blue) 0%, var(--frame-blue-dark) 100%);
    box-shadow: 0 6px 18px rgba(0,0,0,.18);
  }
  .card-face {
    position: absolute; inset: 38px;
    background: var(--card-white);
    border-radius: 44px;
    border: 7px solid var(--edge-grey);
    box-shadow: inset 0 0 14px rgba(0,0,0,.12);
  }
  .brand {
    position: absolute; top: 70px; left: 0; right: 0;
    display: flex; justify-content: center; align-items: center; gap: 18px;
  }
  .brand-dot {
    width: 64px; height: 64px; border-radius: 50%;
    background: var(--brand-red);
  }
  .brand-name {
    font-weight: 800; font-size: 64px; letter-spacing: 1px;
    color: var(--brand-red); line-height: 1;
  }
  .contact-block {
    position: absolute; top: 262px; left: 0; right: 0;
    display: flex; justify-content: center;
  }
  .identity {
    width: 270px; text-align: right; padding-right: 22px;
    color: var(--text-dark);
  }
  .identity-name {
    font-weight: 700; font-size: 26px; color: var(--name-blue);
    margin-bottom: 30px; margin-top: 6px;
  }
  .identity-address { font-size: 19px; line-height: 1.35; }
  .divider { width: 2px; background: var(--divider); }
  .contact-list {
    list-style: none; padding-left: 14px; width: 320px;
    color: var(--text-dark); font-size: 19px;
  }
  .contact-list li {
    display: flex; align-items: center; gap: 8px;
    height: 30px;
  }
  .contact-icon { width: 22px; height: 22px; flex: none; }
</style>
</head>
<body>
  <div class="business-card">
    <div class="card-face">
      <div class="brand">
        <span class="brand-dot"></span>
        <span class="brand-name">HAULVEX 514K</span>
      </div>

      <div class="contact-block">
        <div class="identity">
          <p class="identity-name">Oleksa</p>
          <p class="identity-address">Beijing, Lunmao<br>Plaza C4-517K</p>
        </div>
        <div class="divider"></div>
        <ul class="contact-list">
          <li>
            <svg class="contact-icon" viewBox="0 0 22 22" aria-hidden="true">
              <circle cx="11" cy="11" r="11" fill="var(--icon-blue)"/>
              <path d="M7 6.5c.6-.6 1.4-.5 1.8.1l1 1.6c.3.5.2 1-.2 1.4l-.6.5c.6 1.3 1.5 2.2 2.8 2.8l.5-.6c.4-.4 1-.5 1.4-.2l1.6 1c.6.4.7 1.2.1 1.8l-.7.7c-.8.8-3 .3-5.2-1.9S5.5 8 6.3 7.2z" fill="#fff"/>
            </svg>
            +86-10-55507318
          </li>
          <li>
            <svg class="contact-icon" viewBox="0 0 22 22" aria-hidden="true">
              <circle cx="11" cy="11" r="11" fill="var(--icon-blue)"/>
              <rect x="7.5" y="5" width="7" height="12" rx="1.3" fill="#fff"/>
              <rect x="8.7" y="6.5" width="4.6" height="7.5" fill="var(--icon-blue)"/>
            </svg>
            +86-13955502871
          </li>
          <li>
            <svg class="contact-icon" viewBox="0 0 22 22" aria-hidden="true">
              <circle cx="11" cy="11" r="11" fill="var(--icon-blue)"/>
              <rect x="5.5" y="7" width="11" height="8" rx="1" fill="#fff"/>
              <path d="M5.8 7.4 11 11.4l5.2-4" fill="none" stroke="var(--icon-blue)" stroke-width="1.2"/>
            </svg>
            beijing@haulvex514k.com
          </li>
          <li>
            <svg class="contact-icon" viewBox="0 0 22 22" aria-hidden="true">
              <circle cx="11" cy="11" r="11" fill="var(--icon-blue)"/>
              <g fill="none" stroke="#fff" stroke-width="1.2">
                <circle cx="11" cy="11" r="5.5"/>
                <ellipse cx="11" cy="11" rx="2.3" ry="5.5"/>
                <path d="M5.5 11h11"/>
              </g>
            </svg>
            www.haulvex514k.com
          </li>
        </ul>
      </div>
    </div>
  </div>
</body>
</html>
```